Graffiti Wall Art for Clothing Store

The shape of the artwork should be circle in 2m x 2m dimension.

The design I need is to cover a wall in my store called Plova Tots.

I will be selling footwear for teens to young adults like Quib, Mr.Feldows, Crest Of Elms, Gravelhook, Norventis, etc.

I want the design to be in graffiti of different words that I will put below.

- Plova Tots
- plovatots.com.au

For more design ideas, you may refer to the images below.

Target Market(s)

Kids and young adults

Requirements
Must have
• An edgy, urban, street feel.
Behind the circle artwork needs to be a wall of graffiti writing with Plovatots.com.au, info@plovatots.com.au, Plovatots repeated for the entire wall just like the Henri Delacque file I have attached.

```html
<!DOCTYPE html>
<html lang="en">
<head>
<meta charset="utf-8">
<title>Plova Tots — Circular Wall Art</title>
<link rel="stylesheet" href="https://fonts.googleapis.com/css2?family=Big+Shoulders+Display:wght@800&family=Bungee&family=Lilita+One&family=Montserrat:wght@300;400;900&family=Nunito:wght@900&family=Poppins:wght@500&family=Rubik+Mono+One&family=Titan+One&display=swap">
<style>
  :root{
    --ring:#ead3e8;
    --ring-soft:#f4e6f2;
    --red:#ee3e36;
    --grey:#7b7b7d;
    --yellow:#fcc32c;
    --green:#0aa14b;
    --purple:#6e2c8f;
    --magenta:#ec1c8e;
    --orange:#f7941d;
    --blue:#2aa6df;
  }
  html,body{margin:0;padding:0;overflow:hidden;background:#fff;}
  .wall-art{display:block;width:1200px;height:1200px;}
  .mono-small{font-family:"Montserrat",sans-serif;font-weight:400;font-size:30px;}
  .rounded-bold{font-family:"Nunito",sans-serif;font-weight:900;font-size:66px;}
  .outline-caps{font-family:"Poppins",sans-serif;font-weight:500;font-size:64px;fill:none;stroke-width:2.4;}
  .chunky-caps{font-family:"Titan One",sans-serif;font-size:70px;}
  .thin-caps{font-family:"Montserrat",sans-serif;font-weight:300;font-size:62px;}
  .condensed-caps{font-family:"Big Shoulders Display",sans-serif;font-weight:800;font-size:72px;}
  .block-caps{font-family:"Rubik Mono One",sans-serif;font-size:74px;}
  .heavy-caps{font-family:"Montserrat",sans-serif;font-weight:900;font-size:66px;}
  .brand-name{font-family:"Lilita One",sans-serif;fill:var(--red);}
  .brand-domain{font-family:"Lilita One",sans-serif;fill:var(--red);}
  .c-name{fill:var(--magenta);}
  .c-name-alt{fill:var(--purple);}
  .c-name-yellow{fill:var(--orange);}
  .c-name-green{fill:var(--green);}
  .c-domain{fill:var(--grey);}
  .s-name{stroke:var(--magenta);}
  .s-domain{stroke:var(--grey);}
  .condensed-green{fill:var(--green);}
  .star-orange{fill:var(--orange);}
  .star-red{fill:var(--red);}
</style>
</head>
<body>
<svg class="wall-art" viewBox="0 0 1200 1200" xmlns="http://www.w3.org/2000/svg">
  <defs>
    <radialGradient id="centreGlow" cx="50%" cy="50%" r="50%">
      <stop offset="0" stop-color="#ffffff"/>
      <stop offset="0.75" stop-color="#ffffff"/>
      <stop offset="1" stop-color="#ffffff" stop-opacity="0"/>
    </radialGradient>
  </defs>

  <!-- circular brush backdrop -->
  <g class="backdrop">
    <circle cx="600" cy="605" r="555" fill="var(--ring)"/>
    <circle cx="600" cy="605" r="575" fill="none" stroke="var(--ring-soft)" stroke-width="6"/>
    <circle cx="610" cy="610" r="470" fill="none" stroke="#ffffff" stroke-width="3" opacity="0.7"/>
    <circle cx="610" cy="610" r="430" fill="url(#centreGlow)"/>
  </g>

  <!-- clothing decorations -->
  <g class="clothing">
    <rect role="img" aria-label="Pair of brown baby shoes" x="400" y="104" width="64" height="60" rx="24" fill="#b07a62"/>
    <rect role="img" aria-label="Mint polka-dot dress on a hanger" x="772" y="100" width="72" height="84" rx="18" fill="#6cc9b8"/>
    <rect role="img" aria-label="Pair of mint baby booties" x="204" y="308" width="108" height="76" rx="30" fill="#8ed3c8"/>
    <rect role="img" aria-label="Pink star top" x="140" y="388" width="96" height="100" rx="20" fill="#f29bbd"/>
    <rect role="img" aria-label="Pink star trousers" x="124" y="488" width="76" height="88" rx="16" fill="#f5a3c0"/>
    <rect role="img" aria-label="Mint polka-dot dress" x="112" y="564" width="144" height="172" rx="40" fill="#6cc9b8"/>
    <rect role="img" aria-label="Pink baby bib" x="240" y="588" width="60" height="60" rx="28" fill="#f5a3c0"/>
    <rect role="img" aria-label="Pair of pink baby shoes" x="316" y="592" width="92" height="88" rx="30" fill="#f6bcd3"/>
    <rect role="img" aria-label="Orange fox romper" x="988" y="356" width="100" height="136" rx="26" fill="#f7941d"/>
    <rect role="img" aria-label="Pair of brown lace-up shoes" x="876" y="436" width="140" height="136" rx="40" fill="#a9735e"/>
    <rect role="img" aria-label="Pair of pink baby shoes" x="1048" y="524" width="92" height="92" rx="30" fill="#f6bcd3"/>
    <rect role="img" aria-label="Blue denim jeans" x="972" y="624" width="84" height="108" rx="12" fill="#5b7fb5"/>
    <rect role="img" aria-label="Purple overalls" x="148" y="824" width="72" height="112" rx="16" fill="#9a62b0"/>
    <rect role="img" aria-label="Blue striped onesie" x="968" y="828" width="104" height="152" rx="30" fill="#b9d2ec"/>
    <rect role="img" aria-label="Blue denim jeans" x="292" y="956" width="84" height="112" rx="12" fill="#5b7fb5"/>
  </g>

  <!-- stars -->
  <g class="stars">
    <polygon class="star-orange" transform="translate(336 396) scale(20)" points="0,-1 0.24,-0.31 0.95,-0.31 0.38,0.12 0.59,0.81 0,0.38 -0.59,0.81 -0.38,0.12 -0.95,-0.31 -0.24,-0.31"/>
    <polygon class="star-orange" transform="translate(1020 584) scale(26)" points="0,-1 0.24,-0.31 0.95,-0.31 0.38,0.12 0.59,0.81 0,0.38 -0.59,0.81 -0.38,0.12 -0.95,-0.31 -0.24,-0.31"/>
    <polygon class="star-orange" transform="translate(880 852) scale(26)" points="0,-1 0.24,-0.31 0.95,-0.31 0.38,0.12 0.59,0.81 0,0.38 -0.59,0.81 -0.38,0.12 -0.95,-0.31 -0.24,-0.31"/>
    <polygon class="star-red" transform="translate(868 1060) scale(26)" points="0,-1 0.24,-0.31 0.95,-0.31 0.38,0.12 0.59,0.81 0,0.38 -0.59,0.81 -0.38,0.12 -0.95,-0.31 -0.24,-0.31"/>
  </g>

  <!-- domain lines -->
  <g class="domain-lines">
    <text class="mono-small" x="476" y="148" textLength="288" lengthAdjust="spacingAndGlyphs"><tspan class="c-name">PLOVATOTS</tspan><tspan class="c-domain">.COM.AU</tspan></text>

    <text class="rounded-bold" x="328" y="216" textLength="608" lengthAdjust="spacingAndGlyphs"><tspan class="c-name-yellow">plovatots</tspan><tspan class="c-domain">.com.au</tspan></text>

    <text class="outline-caps" x="288" y="286" textLength="722" lengthAdjust="spacingAndGlyphs"><tspan class="s-name">PLOVATOTS</tspan><tspan class="s-domain">.COM.AU</tspan></text>

    <text class="chunky-caps" x="328" y="358" textLength="668" lengthAdjust="spacingAndGlyphs"><tspan class="c-name-green">PLOVATOTS</tspan><tspan class="c-domain">.COM.AU</tspan></text>

    <text class="thin-caps" x="376" y="430" textLength="580" lengthAdjust="spacingAndGlyphs"><tspan class="c-name-alt">PLOVATOTS</tspan><tspan class="c-domain">.COM.AU</tspan></text>

    <text class="condensed-caps" x="428" y="656" textLength="532" lengthAdjust="spacingAndGlyphs"><tspan class="c-name-yellow">PLOVATOTS</tspan><tspan class="c-domain">.COM.AU</tspan></text>

    <text class="mono-small" x="676" y="702" textLength="288" lengthAdjust="spacingAndGlyphs"><tspan class="c-name">PLOVATOTS</tspan><tspan class="c-domain">.COM.AU</tspan></text>

    <text class="block-caps" x="144" y="812" textLength="888" lengthAdjust="spacingAndGlyphs"><tspan class="c-name">PLOVATOTS</tspan><tspan class="c-domain">.COM.AU</tspan></text>

    <text class="rounded-bold" x="224" y="872" textLength="608" lengthAdjust="spacingAndGlyphs"><tspan class="c-name-alt">plovatots</tspan><tspan class="c-domain">.com.au</tspan></text>

    <text class="heavy-caps" x="244" y="936" textLength="716" lengthAdjust="spacingAndGlyphs"><tspan class="c-name">PLOVATOTS</tspan><tspan class="c-domain">.COM.AU</tspan></text>

    <text class="condensed-caps condensed-green" x="408" y="1076" textLength="416" lengthAdjust="spacingAndGlyphs">PLOVATOTS.COM.AU</text>
  </g>

  <!-- brand name lockups -->
  <g class="brand-names">
    <text class="brand-name" x="232" y="560" font-size="140" textLength="632" lengthAdjust="spacingAndGlyphs">Plova Tots</text>
    <text class="brand-domain" x="788" y="580" font-size="34" textLength="136" lengthAdjust="spacingAndGlyphs">.com.au</text>

    <text class="brand-name" x="264" y="742" font-size="84" textLength="396" lengthAdjust="spacingAndGlyphs">Plovatots</text>
    <text class="brand-domain" x="672" y="740" font-size="40" textLength="260" lengthAdjust="spacingAndGlyphs">.com.au</text>

    <text class="brand-name" x="388" y="1016" font-size="84" textLength="392" lengthAdjust="spacingAndGlyphs">Plovatots</text>
    <text class="brand-domain" x="792" y="1014" font-size="32" textLength="128" lengthAdjust="spacingAndGlyphs">.com.au</text>
  </g>
</svg>
</body>
</html>
```